Innovative Consulting Firm Needs New Business Cards and Stationary

Our Innovative Consulting Firm, Larkfield Consulting, is in need of new business cards and stationary designs. We want two-sided cards that incorporate our logo, which is attached. We are looking for something not too formal, but is professional and slick.

Card should have the following information:
Name (ex. Pat Norwell)
Title (ex. Manager)
Address (ex. 48207 Birch Lane)
Address 2 (ex. Suite 240)
City
State
Zip Code
Mobile
Email

The card should also have our website: www.larkfieldconsulting.example

Industry/Entity Type

Management Consulting

Contact Information for Business Card

Name (ex. Pat Norwell)
Title (ex. Manager)
Address 2 (ex. Suite 240)
City
State
Zip Code
Mobile
Email

Font styles to use
Sans Serif

Requirements
Must have
• The colors on the card must match the colors in the logo. The exact color codes are attached in a pdf.
Nice to have
• The Company's Tagline is "Focused on your Future". This might be nice to incorporate, but not necessary.

```html
<!DOCTYPE html>
<html lang="en">
<head>
<meta charset="utf-8">
<title>Larkfield Consulting – Business Card</title>
<link rel="stylesheet" href="https://fonts.googleapis.com/css2?family=Open+Sans:wght@400;600;700&family=Montserrat:wght@500&display=swap">
<style>
  :root {
    --brand-blue: #22527f;
    --brand-navy: #1f3f66;
    --brand-gold: #f0a81c;
    --card-face: #f7f6f5;
    --backdrop: #e9e6e3;
    --text-light: #ffffff;
    --ghost: rgba(40, 60, 90, 0.18);
  }
  * { box-sizing: border-box; margin: 0; padding: 0; }
  html, body { width: 1200px; height: 900px; overflow: hidden; }
  body {
    background: var(--backdrop);
    font-family: "Open Sans", Arial, sans-serif;
    position: relative;
  }
  .card {
    position: absolute;
    width: 556px;
    height: 343px;
    background: var(--card-face);
    box-shadow: 0 6px 18px rgba(0,0,0,0.12);
    overflow: hidden;
  }
  .card--front { left: 238px; top: 62px; }
  .card--back  { left: 458px; top: 518px; width: 560px; }

  .card__brand {
    position: absolute;
    left: 0; right: 0; top: 0;
    height: 185px;
    display: flex;
    align-items: center;
    justify-content: center;
    gap: 14px;
  }
  .brand-dot {
    width: 22px; height: 22px;
    border-radius: 50%;
    background: var(--brand-gold);
  }
  .brand-name {
    font-family: "Open Sans", Arial, sans-serif;
    font-weight: 600;
    font-size: 40px;
    letter-spacing: 0.5px;
    color: var(--brand-navy);
  }
  .card--back .brand-name { color: var(--ghost); }
  .card--back .brand-dot { background: rgba(240,168,28,0.25); }

  .card__band {
    position: absolute;
    left: 0; right: 0; bottom: 0;
    background: var(--brand-blue);
    color: var(--text-light);
  }
  .card--front .card__band { height: 158px; }
  .card--back .card__band {
    height: 156px;
    display: flex;
    align-items: center;
    justify-content: center;
  }

  .holder {
    position: absolute;
    left: 31px; top: 52px;
  }
  .holder__name { font-weight: 700; font-size: 18px; line-height: 22px; }
  .holder__title { font-size: 14px; line-height: 20px; }

  .address {
    position: absolute;
    left: 144px; top: 43px;
    font-size: 14.5px;
    line-height: 20px;
  }
  .contacts {
    position: absolute;
    left: 297px; top: 44px;
    list-style: none;
    font-size: 14.5px;
    line-height: 20px;
  }
  .contacts li { display: flex; align-items: center; gap: 8px; }
  .contacts svg { width: 11px; height: 11px; flex: none; }

  .tagline {
    font-family: "Montserrat", Arial, sans-serif;
    font-weight: 500;
    font-size: 19px;
    letter-spacing: 1px;
    text-transform: uppercase;
    margin-top: 14px;
  }
</style>
</head>
<body>

  <section class="card card--front" aria-label="Business card front">
    <div class="card__brand">
      <span class="brand-dot" aria-hidden="true"></span>
      <span class="brand-name">Larkfield Consulting</span>
    </div>
    <div class="card__band">
      <div class="holder">
        <p class="holder__name">Pat Norwell</p>
        <p class="holder__title">Manager</p>
      </div>
      <address class="address" style="font-style:normal">
        48207 Birch Lane<br>
        Suite 240, City<br>
        State, Zip Code
      </address>
      <ul class="contacts">
        <li>
          <svg viewBox="0 0 12 12" aria-hidden="true"><rect x="3" y="0.5" width="6" height="11" rx="1.2" fill="none" stroke="#fff" stroke-width="1.2"/><circle cx="6" cy="9.4" r="0.7" fill="#fff"/></svg>
          055-987 654 321
        </li>
        <li>
          <svg viewBox="0 0 12 12" aria-hidden="true"><rect x="1" y="2.5" width="10" height="7" fill="#fff"/><path d="M1 2.5 L6 6.5 L11 2.5" fill="none" stroke="#22527f" stroke-width="1"/></svg>
          hello@larkfield.example
        </li>
        <li>
          <svg viewBox="0 0 12 12" aria-hidden="true"><circle cx="6" cy="6" r="5" fill="#fff"/><path d="M1 6 H11 M6 1 C3.5 4 3.5 8 6 11 M6 1 C8.5 4 8.5 8 6 11" fill="none" stroke="#22527f" stroke-width="0.8"/></svg>
          www.larkfieldconsulting.example
        </li>
      </ul>
    </div>
  </section>

  <section class="card card--back" aria-label="Business card back">
    <div class="card__brand">
      <span class="brand-name">Larkfield Consulting</span>
      <span class="brand-dot" aria-hidden="true"></span>
    </div>
    <div class="card__band">
      <p class="tagline">Focused on your future</p>
    </div>
  </section>

</body>
</html>
```